Rimah Advertising & Publicity business cards

I would like my Company's business card to be designed creatively & profissionally the logo is attached in both Arabic & english and prefer to have my emblem dimmed on the card as well
-Logo ( Arabic & English)
-Name (Arabic & English)
-Title ( Arabic & English)
-----------
-Location
-Landline (icon)
-Mobile phone (icon)
-Email (icon)
-Instagram (icon)
-WhatsApp (icon)

Target Market(s)

Industry/Entity Type

Marketing

Contact Information for Business Card

-Logo ( Arabic & English)
-Name (Arabic & English)
-----------
-Location
-Landline (icon)
-Mobile phone (icon)
-Email (icon)
-Instagram (icon)
-WhatsApp (icon)

Font styles to use
Serif

Requirements
Must have
• all what is mentions in business card details blanked and i will add the data my self
Nice to have
• Dim emblem on my business card both Arabic & english

```html
<!DOCTYPE html>
<html lang="ar">
<head>
<meta charset="utf-8">
<title>Rimah Advertising &amp; Publicity – Business Cards</title>
<link rel="stylesheet" href="https://fonts.googleapis.com/css2?family=Cairo:wght@400;700&family=Open+Sans:wght@600&display=swap">
<style>
  :root {
    --stage: #1c2028;
    --teal: #3aa9b4;
    --teal-deep: #2a95a2;
    --teal-light: #7fd0d4;
    --grey: #8a8a8a;
    --ink: #1a1a1a;
    --paper: #ffffff;
  }
  * { box-sizing: border-box; margin: 0; padding: 0; }
  html, body { width: 1200px; height: 1000px; overflow: hidden; }
  body {
    background: var(--stage);
    font-family: "Cairo", sans-serif;
    position: relative;
  }
  .card {
    position: absolute;
    width: 700px;
    height: 420px;
    overflow: hidden;
    box-shadow: 0 12px 30px rgba(0,0,0,.5);
  }
  /* front */
  .card-front { left: 70px; top: 60px; background: var(--paper); }
  .card-front .waves { position: absolute; inset: 0; }
  .brand {
    position: absolute; left: 40px; top: 28px;
    display: flex; align-items: center; gap: 12px;
  }
  .brand-text { text-align: center; color: var(--ink); }
  .brand-name { font-size: 34px; font-weight: 700; line-height: 1.1; }
  .brand-tag { font-size: 11px; font-weight: 700; }
  .brand-rule { width: 1px; height: 60px; background: var(--grey); }
  .brand-mark { width: 46px; height: 46px; border-radius: 50%; background: var(--teal); }
  .details {
    position: absolute; right: 28px; top: 158px;
    direction: rtl; text-align: right; color: var(--ink);
  }
  .person-name { font-size: 22px; font-weight: 700; line-height: 1.3; }
  .person-title { font-size: 9px; font-weight: 700; color: var(--teal); margin: 8px 0 8px; }
  .info-line { font-size: 12px; font-weight: 700; line-height: 2; }
  .contacts { margin-top: 10px; }
  .contact { display: flex; align-items: center; gap: 8px; font-size: 12px; font-weight: 700; height: 30px; }
  .contact.phone { font-size: 15px; direction: ltr; justify-content: flex-end; flex-direction: row-reverse; }
  .contact-row { display: flex; gap: 40px; }
  .icon { width: 17px; height: 17px; border-radius: 50%; background: var(--teal); flex: none; display: grid; place-items: center; }
  .icon svg { width: 11px; height: 11px; }
  .website {
    position: absolute; left: 218px; bottom: 8px;
    font-family: "Open Sans", sans-serif; font-weight: 600;
    font-size: 18px; letter-spacing: 1.5px; color: var(--paper);
  }
  /* back */
  .card-back {
    left: 370px; top: 500px;
    background: radial-gradient(circle at 35% 20%, var(--teal-light) 0%, var(--teal) 45%, var(--teal-deep) 100%);
    color: var(--paper); text-align: center;
  }
  .ghost-name {
    position: absolute; left: 14px; top: 4px;
    font-family: "Cairo", sans-serif; font-size: 46px; font-weight: 400;
    color: rgba(255,255,255,.12);
  }
  .back-name { position: absolute; left: 0; right: 0; top: 120px; font-size: 64px; font-weight: 700; line-height: 1; }
  .back-tag { position: absolute; left: 0; right: 0; top: 290px; font-size: 32px; font-weight: 700; }
</style>
</head>
<body>

<section class="card card-front" aria-label="Business card front">
  <svg class="waves" viewBox="0 0 700 420" aria-hidden="true">
    <path d="M215,0 C390,8 500,120 700,150 L700,0 Z" fill="var(--grey)"/>
    <path d="M245,0 C410,10 520,112 700,138 L700,0 Z" fill="var(--teal)"/>
    <path d="M0,245 C110,330 300,360 700,372 L700,390 C300,380 120,355 0,285 Z" fill="var(--grey)"/>
    <path d="M0,268 C120,345 300,374 700,384 L700,420 L0,420 Z" fill="var(--teal)"/>
  </svg>

  <div class="brand">
    <div class="brand-text">
      <div class="brand-name">رِماح</div>
      <div class="brand-tag">للدعاية والإعلان</div>
    </div>
    <div class="brand-rule"></div>
    <div class="brand-mark"></div>
  </div>

  <div class="details">
    <div class="person-name">ا قس م فـل اوف كـنـة ن</div>
    <div class="person-title">المسمى الوظيفي</div>
    <div class="info-line">ا قس م فـل اوف كـنـة ن ا قس م فـل اوف كـنـة ن</div>
    <div class="info-line">ا قس م فـل اوف كـنـة ن</div>
    <div class="contacts">
      <div class="contact phone">
        <span class="icon"><svg viewBox="0 0 12 12"><path d="M3 1 L5 3.5 L4 5 C4.8 6.6 5.6 7.4 7 8 L8.5 7 L11 9 L10 11 C5 10.5 1.5 7 1 2 Z" fill="#fff"/></svg></span>
        <span>0321455600)</span>
      </div>
      <div class="contact">
        <span class="icon"><svg viewBox="0 0 12 12"><rect x="1.5" y="3" width="9" height="6.5" fill="none" stroke="#fff"/><path d="M1.5 3 L6 7 L10.5 3" fill="none" stroke="#fff"/></svg></span>
        <span>ا قس م فـل اوف كـنـة ن</span>
      </div>
      <div class="contact-row">
        <div class="contact"><span class="icon"></span><span>ا قس م فـل اوف كـنـة ن</span></div>
        <div class="contact"><span class="icon"></span><span>ا قس م فـل اوف كـنـة ن</span></div>
      </div>
    </div>
  </div>

  <div class="website">WWW.RIMAHADS.COM</div>
</section>

<section class="card card-back" aria-label="Business card back">
  <div class="ghost-name">Rimah</div>
  <div class="back-name">رِماح</div>
  <div class="back-tag">للدعاية والإعلان</div>
</section>

</body>
</html>
```